Label and logo design for organic food range

We are looking to a new label and logo design for a brand new range of organic foods. We have a conventional product range branded as veldhoeve and we are launching a new line of organic products under the brandname "naturavel"

For reference I attached the logo of veldhoeve which we like it very much, but we think that we would need an upgraded, more fresh logo design for our new brand.

I also attached a label for a veldhoeve product, we use only one label on the products (packed in transparent bags), so the label must contains a lot of text and informations as you can see on the veldhoeve label. (mostly it should contain all the text on the label attached)

Target Market(s)

organic products, bio products, health stores

Industry/Entity Type

Health Product

Logo Text

the healthy choice

Font styles to use
Sans Serif
Other font styles liked:
• CabinSketch, Bebas Neue, Chalkboard,

Colors
9bcb3b
00a990
fbed22
f78f20
faa54b
fac994
f37122
f68d4d
ec1f27

Requirements
Nice to have
• As a reference, I attached 3 labels (same brand I like very much, 1,2,3.jpg). Default label size is 64mm x 100mm ( + 2.5mm bleed). I also attached the texts on the label (label-text.docx)

```html
<!DOCTYPE html>
<html lang="ro">
<head>
<meta charset="utf-8">
<title>naturavel Organic – etichetă migdale</title>
<link rel="stylesheet" href="https://fonts.googleapis.com/css2?family=Oswald:wght@700&family=Open+Sans:wght@400;600;700&family=Kaushan+Script&display=swap">
<style>
  :root {
    --page: #ffffff;
    --burlap-light: #f6ead0;
    --burlap-dark: #e9d8b3;
    --green-dark: #2f6a10;
    --green-mid: #4f9a12;
    --green-light: #8fe31e;
    --ink-white: #ffffff;
    --shadow: #9a9a9a;
  }
  * { box-sizing: border-box; margin: 0; padding: 0; }
  html, body { width: 1200px; height: 909px; overflow: hidden; background: var(--page); }
  body { position: relative; font-family: "Open Sans", sans-serif; }

  .label {
    position: absolute; left: 363px; top: 84px; width: 474px; height: 740px;
    background: radial-gradient(ellipse at 40% 40%, var(--burlap-light), var(--burlap-dark));
    box-shadow: 9px 9px 0 var(--shadow);
    overflow: hidden;
  }
  .label > * { position: absolute; }

  .brand-name {
    left: 30px; top: 6px; width: 420px;
    font-family: "Oswald", sans-serif; font-weight: 700; font-size: 104px; line-height: 1;
    color: var(--green-dark); letter-spacing: -1px; text-align: center;
  }
  .brand-range {
    left: 262px; top: 126px;
    font-family: "Kaushan Script", cursive; font-size: 46px; color: var(--green-dark);
  }

  .stem {
    left: 228px; top: 118px; width: 18px; height: 622px;
    background: var(--green-light);
  }

  .leaf {
    color: var(--ink-white); font-size: 12.5px; line-height: 1.2;
    padding: 12px 14px;
  }
  .leaf b { font-weight: 700; }
  .leaf-left {
    left: 14px; width: 216px;
    background: linear-gradient(90deg, var(--green-dark), var(--green-mid) 45%, var(--green-light));
    border-radius: 70px 0 0 70px / 60px 0 0 60px;
  }
  .leaf-right {
    left: 244px; width: 218px;
    background: linear-gradient(90deg, var(--green-light), var(--green-mid) 55%, var(--green-dark));
    border-radius: 0 90px 0 90px / 0 70px 0 70px;
  }

  .usage { top: 156px; height: 124px; text-align: right; }
  .usage .leaf-title { text-align: left; margin-bottom: 4px; }
  .ingredients { top: 216px; height: 152px; padding: 14px 14px 10px 14px; }
  .ingredients p { margin-bottom: 3px; }
  .ingredients .leaf-title { text-align: center; }
  .facility { top: 430px; height: 82px; text-align: center; padding-top: 12px; }
  .facility .info-dot {
    display: inline-block; width: 13px; height: 13px; background: var(--green-light);
    border-radius: 3px; vertical-align: -2px; margin-right: 3px;
  }
  .distributor { top: 560px; height: 82px; padding-top: 12px; text-align: center; }

  .organic-badge {
    left: 60px; top: 314px; width: 94px; height: 62px; background: var(--green-light);
  }
  .badge-caption { left: 60px; top: 381px; width: 94px; font-size: 9.5px; text-align: center; color: #333; }

  .net-weight { left: 96px; top: 530px; font-weight: 700; font-size: 24px; color: var(--green-dark); }
  .symbols { left: 46px; top: 572px; display: flex; gap: 10px; }
  .symbols span { width: 30px; height: 30px; border: 3px solid var(--green-dark); border-radius: 50%; }
  .symbols span:nth-child(3) { border-radius: 4px; }

  .nutrition-title { left: 272px; top: 392px; font-size: 12px; font-weight: 700; color: var(--green-dark); }
  .nutrition-table {
    left: 272px; top: 414px; width: 176px; height: 120px;
    border: 3px solid var(--green-dark); border-collapse: collapse;
    font-size: 10px; color: var(--green-dark);
  }
  .nutrition-table td { border: 2px solid var(--green-dark); height: 15px; padding: 0 6px; font-weight: 700; }
  .nutrition-table td:last-child { text-align: right; font-size: 8.5px; }

  .web { left: 290px; top: 660px; font-size: 18px; font-weight: 700; color: var(--green-dark); display: flex; align-items: center; gap: 6px; }
  .social { top: 690px; }
  .dot { width: 20px; height: 20px; border: 2.5px solid var(--green-dark); border-radius: 50%; }
</style>
</head>
<body>
  <article class="label">
    <div class="brand-name">naturavel</div>
    <div class="brand-range">Organic</div>
    <div class="stem"></div>

    <section class="leaf leaf-left usage">
      <p class="leaf-title"><b>Mod de utilizare:</b></p>
      <p>Se pot consuma ca atare sau prăjite în diverse combinații cu legume, sosuri, cereale și deserturi. A se consuma, de preferință, înainte de data marcată pe ambalaj.</p>
    </section>

    <section class="leaf leaf-right ingredients">
      <p class="leaf-title"><b>Ingrediente:</b></p>
      <p style="text-align:center">sâmburi de Migdale crude.</p>
      <p><b>Depozitare:</b> A se păstra la loc uscat și răcoros.</p>
      <p><b>Atenționare:</b> produsul conține substanțe cu potențial alergen: <b>migdale.</b></p>
      <p><b>Țara de origine:</b> SUA.</p>
    </section>

    <div class="organic-badge" role="img" aria-label="Sigla de produs ecologic"></div>
    <div class="badge-caption">Text goes here...</div>

    <section class="leaf leaf-left facility">
      <p><span class="info-dot"></span>Produs într-o unitate care ambalează și procesează făină din cereale, muștar, soia, nuci, alune, semințe de susan.</p>
    </section>

    <div class="net-weight">250g</div>
    <div class="symbols" role="img" aria-label="Simboluri de reciclare și ambalare"><span></span><span></span><span></span><span></span></div>

    <div class="nutrition-title">VALORI NUTRIȚIONALE / 100G:</div>
    <table class="nutrition-table">
      <tr><td>Energie:</td><td>2728kJ/659kcal</td></tr>
      <tr><td>Grăimi:</td><td>55,8 g</td></tr>
      <tr><td></td><td></td></tr>
      <tr><td></td><td></td></tr>
      <tr><td></td><td></td></tr>
      <tr><td></td><td></td></tr>
      <tr><td></td><td></td></tr>
    </table>

    <section class="leaf leaf-right distributor">
      <p><b>Distribuitor:</b></p>
      <p><b>Verdalis Trade SRL</b></p>
      <p>Oradea, str. Livezii 14</p>
      <p style="text-align:left"><b>Ambalat in Romania</b></p>
    </section>

    <div class="web"><span class="dot"></span>naturavel.ro</div>
    <div class="web social"><span class="dot"></span>/naturavel</div>
  </article>
</body>
</html>
```